Poster of Core Values & Motto

Create our core values poster and motto. Attached are our core values and our Motto. This poster represents both of our companies Tidy Pulp & CuraBinix.

Target Market(s)

Our team / employees

Industry/Entity Type

Shredding and Medical Waste

Colors
59FF00
82FF00
B8FF75
E3FFCB
F4FFEA
EB3D1F
EC4F4E
F09395
F8D3D4
FCEDEE

Requirements
Must have
• Include both companies logos

```html
<!DOCTYPE html>
<html lang="en">
<head>
<meta charset="utf-8">
<title>Core Values &amp; Motto</title>
<link rel="stylesheet" href="https://fonts.googleapis.com/css2?family=Oswald:wght@600;700&family=Kanit:wght@400;500;600&display=swap">
<style>
  :root {
    --page-bg: #dcdcdc;
    --paper: #ffffff;
    --header-red: #eb3d1f;
    --swoosh-green: #7fd843;
    --ring-grey: #c9cdd0;
    --ink: #222222;
    --core-red: #e0545a;
    --v1-purple: #ae4fb3;
    --v2-orange: #f06a22;
    --v3-blue: #5563ad;
    --v4-green: #7ed84d;
    --v5-cyan: #13b7de;
    --v6-red: #e35b5e;
    --brand-dark: #2a2a2a;
    --brand-green: #4fbf1a;
  }
  * { margin: 0; padding: 0; box-sizing: border-box; }
  html, body { width: 1200px; height: 1200px; overflow: hidden; }
  body { background: var(--page-bg); position: relative; }
  .poster {
    position: absolute; left: 212px; top: 18px;
    width: 776px; height: 1164px; display: block;
    background: var(--paper);
    box-shadow: 0 4px 14px rgba(0,0,0,.18);
  }
  .title { font-family: "Oswald", "Arial Narrow", sans-serif; font-weight: 700; fill: #fff; }
  .core-word { font-family: "Oswald", "Arial Narrow", sans-serif; font-weight: 700; fill: var(--core-red); }
  .step-num { font-family: "Oswald", "Arial Narrow", sans-serif; font-weight: 700; font-size: 52px; }
  .value-label { font-family: "Kanit", sans-serif; font-weight: 600; font-size: 23px; fill: #fff; }
  .motto { font-family: "Kanit", sans-serif; font-weight: 400; font-size: 27px; fill: var(--ink); }
  .brand { font-family: "Kanit", sans-serif; font-weight: 600; font-size: 62px; }
  .icon-slot { fill: rgba(255,255,255,.2); }
</style>
</head>
<body>
<svg class="poster" viewBox="0 0 1037 1555" xmlns="http://www.w3.org/2000/svg">
  <!-- header -->
  <path class="header-swoosh" d="M40 290 C150 240 300 190 500 178 C650 172 850 250 1037 395 V440 C850 290 650 198 500 196 C310 196 160 240 40 290 Z" fill="var(--swoosh-green)"/>
  <path class="header-band" d="M0 0 H1037 V395 C850 250 650 172 500 176 C300 182 120 240 0 300 Z" fill="var(--header-red)"/>
  <text class="title" x="519" y="134" font-size="118" text-anchor="middle" textLength="875" lengthAdjust="spacingAndGlyphs">CORE VALUES &amp; MOTTO</text>

  <!-- hub -->
  <circle class="outer-arc" cx="172" cy="827" r="325" fill="none" stroke="var(--ring-grey)" stroke-width="5"/>
  <g class="spokes" stroke="var(--ring-grey)" stroke-width="3">
    <line x1="174" y1="827" x2="168" y2="627"/>
    <line x1="174" y1="827" x2="293" y2="667"/>
    <line x1="174" y1="827" x2="364" y2="764"/>
    <line x1="174" y1="827" x2="364" y2="892"/>
    <line x1="174" y1="827" x2="284" y2="995"/>
    <line x1="174" y1="827" x2="167" y2="1029"/>
  </g>
  <g class="spoke-nodes" fill="#fff" stroke="var(--ring-grey)" stroke-width="2">
    <circle cx="168" cy="627" r="7"/><circle cx="293" cy="667" r="7"/>
    <circle cx="364" cy="764" r="7"/><circle cx="364" cy="892" r="7"/>
    <circle cx="284" cy="995" r="7"/><circle cx="167" cy="1029" r="7"/>
  </g>
  <circle class="core-hub" cx="174" cy="827" r="127" fill="#fff" stroke="var(--ring-grey)" stroke-width="15"/>
  <text class="core-word" x="179" y="812" font-size="58" text-anchor="middle">CORE</text>
  <text class="core-word" x="179" y="880" font-size="58" text-anchor="middle">VALUES</text>

  <!-- value 1 -->
  <g class="value" style="--c: var(--v1-purple)">
    <line x1="167" y1="564" x2="167" y2="384" stroke="var(--c)" stroke-width="34"/>
    <circle cx="167" cy="384" r="107" fill="var(--c)"/>
    <circle class="icon-slot" cx="167" cy="342" r="52" role="img" aria-label="Teamwork icon: people with gear and handshake"/>
    <text class="value-label" x="167" y="431" text-anchor="middle">Synergy/</text>
    <text class="value-label" x="167" y="460" text-anchor="middle">Teamwork</text>
    <circle cx="167" cy="564" r="53" fill="var(--c)"/><circle cx="167" cy="564" r="39" fill="#fff"/>
    <text class="step-num" x="167" y="583" text-anchor="middle" fill="var(--c)">1</text>
  </g>
  <!-- value 2 -->
  <g class="value" style="--c: var(--v2-orange)">
    <line x1="331" y1="617" x2="450" y2="479" stroke="var(--c)" stroke-width="34"/>
    <circle cx="450" cy="479" r="107" fill="var(--c)"/>
    <circle class="icon-slot" cx="450" cy="440" r="52" role="img" aria-label="Excellence icon: hand holding a crowned box"/>
    <text class="value-label" x="450" y="543" text-anchor="middle">Excellence</text>
    <circle cx="331" cy="617" r="53" fill="var(--c)"/><circle cx="331" cy="617" r="39" fill="#fff"/>
    <text class="step-num" x="331" y="636" text-anchor="middle" fill="var(--c)">2</text>
  </g>
  <!-- value 3 -->
  <g class="value" style="--c: var(--v3-blue)">
    <line x1="424" y1="744" x2="600" y2="704" stroke="var(--c)" stroke-width="34"/>
    <circle cx="600" cy="704" r="107" fill="var(--c)"/>
    <circle class="icon-slot" cx="600" cy="664" r="52" role="img" aria-label="Efficiency icon: hand under a gear with tick"/>
    <text class="value-label" x="600" y="766" text-anchor="middle">Efficient</text>
    <circle cx="424" cy="744" r="53" fill="var(--c)"/><circle cx="424" cy="744" r="39" fill="#fff"/>
    <text class="step-num" x="424" y="763" text-anchor="middle" fill="var(--c)">3</text>
  </g>
  <!-- value 4 -->
  <g class="value" style="--c: var(--v4-green)">
    <line x1="424" y1="912" x2="594" y2="971" stroke="var(--c)" stroke-width="34"/>
    <circle cx="594" cy="971" r="107" fill="var(--c)"/>
    <circle class="icon-slot" cx="594" cy="926" r="52" role="img" aria-label="Security icon: shield with padlock"/>
    <text class="value-label" x="594" y="1017" text-anchor="middle">Safe and</text>
    <text class="value-label" x="594" y="1046" text-anchor="middle">Secure</text>
    <circle cx="424" cy="912" r="53" fill="var(--c)"/><circle cx="424" cy="912" r="39" fill="#fff"/>
    <text class="step-num" x="424" y="931" text-anchor="middle" fill="var(--c)">4</text>
  </g>
  <!-- value 5 -->
  <g class="value" style="--c: var(--v5-cyan)">
    <line x1="319" y1="1049" x2="429" y2="1190" stroke="var(--c)" stroke-width="34"/>
    <circle cx="429" cy="1190" r="107" fill="var(--c)"/>
    <circle class="icon-slot" cx="429" cy="1146" r="52" role="img" aria-label="Integrity icon: balance scale above people"/>
    <text class="value-label" x="429" y="1240" text-anchor="middle">Honesty</text>
    <text class="value-label" x="429" y="1269" text-anchor="middle">Integrity</text>
    <circle cx="319" cy="1049" r="53" fill="var(--c)"/><circle cx="319" cy="1049" r="39" fill="#fff"/>
    <text class="step-num" x="319" y="1068" text-anchor="middle" fill="var(--c)">5</text>
  </g>
  <!-- value 6 -->
  <g class="value" style="--c: var(--v6-red)">
    <line x1="164" y1="1092" x2="163" y2="1264" stroke="var(--c)" stroke-width="34"/>
    <circle cx="163" cy="1264" r="107" fill="var(--c)"/>
    <circle class="icon-slot" cx="163" cy="1222" r="52" role="img" aria-label="Dependability icon: process flow chart"/>
    <text class="value-label" x="163" y="1340" text-anchor="middle">Dependable</text>
    <circle cx="164" cy="1092" r="53" fill="var(--c)"/><circle cx="164" cy="1092" r="39" fill="#fff"/>
    <text class="step-num" x="164" y="1111" text-anchor="middle" fill="var(--c)">6</text>
  </g>

  <!-- mottos -->
  <g class="motto-block">
    <rect x="291" y="267" width="4" height="56" fill="var(--v1-purple)"/>
    <text class="motto" x="314" y="288">Get It Done Attitude</text>
    <text class="motto" x="314" y="322">with Humble confidence</text>

    <rect x="593" y="422" width="4" height="57" fill="var(--v2-orange)"/>
    <text class="motto" x="612" y="443">Exceed expectations</text>
    <text class="motto" x="612" y="478">with a smile</text>

    <rect x="739" y="647" width="4" height="95" fill="var(--v3-blue)"/>
    <text class="motto" x="757" y="668">On-Time, sense</text>
    <text class="motto" x="757" y="702">of urgency,alway</text>
    <text class="motto" x="757" y="736">trying to improve</text>

    <rect x="739" y="887" width="4" height="128" fill="var(--v4-green)"/>
    <text class="motto" x="757" y="908">We are just as</text>
    <text class="motto" x="757" y="942">secure as an</text>
    <text class="motto" x="757" y="976">armored truck</text>
    <text class="motto" x="757" y="1011">with money</text>

    <rect x="569" y="1187" width="4" height="57" fill="var(--v5-cyan)"/>
    <text class="motto" x="590" y="1209">Do the right</text>
    <text class="motto" x="590" y="1243">thing</text>

    <rect x="291" y="1322" width="4" height="56" fill="var(--v6-red)"/>
    <text class="motto" x="314" y="1341">Do what you say</text>
    <text class="motto" x="314" y="1375">you will do</text>
  </g>

  <!-- brands -->
  <line x1="597" y1="1387" x2="1037" y2="1387" stroke="#eeeeee" stroke-width="2"/>
  <text class="brand" x="44" y="1494" fill="var(--brand-dark)" textLength="500" lengthAdjust="spacingAndGlyphs">CuraBinix</text>
  <text class="brand" x="675" y="1494" fill="var(--brand-green)" textLength="320" lengthAdjust="spacingAndGlyphs">Tidy Pulp</text>
</svg>
</body>
</html>
```